Audio Tour Poster

I need a poster to show information on a audio tour ... walk ... bike etc ... the poster needs to be generic so that it could be used for several projects ... a space needs to be left to add a tour title and another area where a tri fold brochure can be placed for people to access ... the tri fold poster will be based on 8.5 x 14 inch legal size ...

The size of the final poster will be 18x 24 inches ... an example of a audio tour can be found at
http://trelvanu.com/walk/568 or http://trelvanu.com/walk/2507

Industry/Entity Type

Legal

```html
<!DOCTYPE html>
<html lang="en">
<head>
<meta charset="utf-8">
<title>Audio Tour Available</title>
<link href="https://fonts.googleapis.com/css2?family=Righteous&family=Oswald:wght@600;700&display=swap" rel="stylesheet">
<style>
  :root {
    --sky-light: #cdebee;
    --sky-mid: #aadde3;
    --sky-deep: #6fc3cf;
    --cream: #fffbea;
    --crimson: #b3202a;
    --rule-grey: #8e9699;
    --rule-light: #e9f6f7;
    --shadow: rgba(40, 60, 70, 0.35);
  }
  * { margin: 0; padding: 0; box-sizing: border-box; }
  html, body { width: 900px; height: 1200px; overflow: hidden; }
  .poster {
    position: relative;
    width: 900px;
    height: 1200px;
    overflow: hidden;
  }
  .backdrop {
    position: absolute;
    inset: 0;
    background:
      radial-gradient(ellipse at 10% 20%, var(--sky-deep) 0%, transparent 45%),
      radial-gradient(ellipse at 85% 90%, rgba(180,190,195,0.45) 0%, transparent 40%),
      radial-gradient(ellipse at 90% 10%, rgba(200,210,212,0.5) 0%, transparent 35%),
      linear-gradient(160deg, var(--sky-mid) 0%, var(--sky-light) 55%, var(--sky-mid) 100%);
  }
  .headline {
    position: absolute;
    inset: 0;
    width: 900px;
    height: 1200px;
  }
  .headline-word {
    font-family: "Righteous", "Arial Black", sans-serif;
    font-size: 150px;
    fill: var(--cream);
    stroke: var(--crimson);
    stroke-width: 3px;
    paint-order: stroke;
    letter-spacing: 2px;
  }
  .tagline {
    position: absolute;
    left: 95px;
    top: 815px;
    width: 340px;
    text-align: center;
    font-family: "Oswald", "Arial Narrow", sans-serif;
    font-weight: 700;
    color: var(--crimson);
    text-transform: uppercase;
    text-shadow: 4px 6px 5px var(--shadow);
    letter-spacing: -0.5px;
  }
  .tagline-line { display: block; font-size: 34px; line-height: 1; }
  .tagline-line + .tagline-line { margin-top: 44px; }
  .tagline-line.emphasis { margin-top: 38px; }
  .tagline-key { font-size: 46px; }
</style>
</head>
<body>
<main class="poster">
  <div class="backdrop" role="img" aria-label="Textured pale turquoise background with soft grey halftone dot swirls"></div>

  <svg class="headline" viewBox="0 0 900 1200" aria-labelledby="headline-title">
    <title id="headline-title">Audio Tour Available</title>
    <defs>
      <filter id="arc-shadow" x="-50%" y="-20%" width="200%" height="140%">
        <feDropShadow dx="4" dy="4" stdDeviation="3" flood-color="#3a5560" flood-opacity="0.45"/>
      </filter>
    </defs>

    <g class="sound-waves" fill="var(--cream)" filter="url(#arc-shadow)">
      <path d="M6 368 Q28 420 14 478 L22 476 Q36 420 14 366 Z"/>
      <path d="M40 336 Q80 420 52 520 L64 518 Q94 420 52 334 Z"/>
      <path d="M84 312 Q138 420 98 550 L114 548 Q156 420 100 310 Z"/>
    </g>

    <g class="rules" stroke-linecap="round">
      <line x1="0" y1="499" x2="790" y2="414" stroke="var(--rule-light)" stroke-width="2"/>
      <line x1="0" y1="497" x2="790" y2="412" stroke="var(--rule-grey)" stroke-width="3"/>
      <line x1="65" y1="627" x2="860" y2="542" stroke="var(--rule-light)" stroke-width="2"/>
      <line x1="65" y1="625" x2="860" y2="540" stroke="var(--rule-grey)" stroke-width="3"/>
      <line x1="150" y1="747" x2="900" y2="677" stroke="var(--rule-light)" stroke-width="2"/>
      <line x1="150" y1="745" x2="900" y2="675" stroke="var(--rule-grey)" stroke-width="3"/>
    </g>

    <g class="headline-words">
      <text class="headline-word" x="132" y="478" transform="rotate(-6 132 478)" textLength="445" lengthAdjust="spacingAndGlyphs">AUDIO</text>
      <text class="headline-word" x="246" y="585" transform="rotate(-6 246 585)" textLength="350" lengthAdjust="spacingAndGlyphs">TOUR</text>
      <text class="headline-word" x="272" y="705" transform="rotate(-6 272 705)" textLength="626" lengthAdjust="spacingAndGlyphs">AVAILABLE</text>
    </g>
  </svg>

  <p class="tagline">
    <span class="tagline-line">Make</span>
    <span class="tagline-line emphasis">The <span class="tagline-key">Most</span></span>
    <span class="tagline-line">Of your visit...</span>
  </p>
</main>
</body>
</html>
```